Online-Marketing Material für Alltagsbegleiter
Zielgruppe
Wir bieten Haushaltshilfen und Alltagsbegleiter für Privathaushalte an. Unsere Hauptkundenklientel sind Pflegebedürftige Menschen denen eine Haushaltshilfe von der Pflegekasse zusteht. Weitere Kunden sind Familien und/oder Singlehaushalte, die eine Haushaltfshilfe benötigen.
Aufgabenstellung
Es soll ein neues Titelbild für unsere Facebokseite erstellt werden. Das Titelbild soll unser Logo enthalten und ggfls. auch ein paar Schrftzüge, bzw. Texte von unserer Internetseite. Das Titelbild soll leicht, locker und modern rüber kommen.

```html
<!DOCTYPE html>
<html lang="de">
<head>
<meta charset="utf-8">
<title>Marenstein – Titelbild</title>
<link rel="stylesheet" href="https://fonts.googleapis.com/css2?family=Cinzel:wght@700;800&display=swap">
<style>
  :root {
    --page-bg: #b9b9b9;
    --brand-red: #c21d2d;
    --brand-red-dark: #9e1622;
    --band-grey: #3f3f42;
    --paper: #ffffff;
    --photo-light: #ece6df;
    --photo-warm: #c58f78;
  }
  html, body {
    margin: 0;
    padding: 0;
    width: 1091px;
    height: 1200px;
    overflow: hidden;
    background: var(--page-bg);
  }
  .canvas {
    width: 1091px;
    height: 1200px;
    display: flex;
    align-items: center;
    justify-content: center;
  }
  .cover {
    width: 1011px;
    height: 374px;
    display: block;
    box-shadow: 0 10px 24px rgba(0,0,0,0.25);
    font-family: "Cinzel", "Trajan Pro", serif;
  }
  .brand-name { font-weight: 800; fill: var(--brand-red); }
  .band-text { font-weight: 800; fill: var(--paper); }
</style>
</head>
<body>
<main class="canvas">
  <svg class="cover" viewBox="0 0 1535 568" xmlns="http://www.w3.org/2000/svg">
    <defs>
      <clipPath id="cover-clip"><rect width="1535" height="568"/></clipPath>
      <linearGradient id="photo-tone" x1="0" y1="0" x2="1" y2="1">
        <stop offset="0" stop-color="var(--photo-light)"/>
        <stop offset="0.45" stop-color="var(--photo-warm)"/>
        <stop offset="0.8" stop-color="#a8735e"/>
        <stop offset="1" stop-color="#e2dcd4"/>
      </linearGradient>
    </defs>
    <g clip-path="url(#cover-clip)">
      <rect class="cover-paper" width="1535" height="568" fill="var(--paper)"/>
      <rect class="red-band" x="0" y="285" width="1100" height="210" fill="var(--brand-red)"/>
      <rect class="grey-band" x="0" y="495" width="1100" height="73" fill="var(--band-grey)"/>

      <circle class="ring-gap" cx="1400" cy="290" r="575" fill="var(--paper)"/>
      <circle class="ring-outer" cx="1400" cy="290" r="560" fill="var(--brand-red)"/>
      <circle class="ring-inner" cx="1410" cy="290" r="535" fill="var(--brand-red-dark)"/>
      <circle class="ring-white" cx="1420" cy="290" r="520" fill="var(--paper)"/>
      <circle class="photo-area" cx="1425" cy="290" r="505" fill="url(#photo-tone)"
              role="img" aria-label="Foto: Hände einer Begleiterin auf der Hand eines älteren Menschen am Griff eines Rollators"/>
    </g>

    <circle class="brand-dot" cx="170" cy="138" r="40" fill="var(--brand-red)"/>
    <text class="brand-name" x="240" y="164" font-size="72" textLength="540" lengthAdjust="spacingAndGlyphs">MARENSTEIN</text>

    <text class="band-text" x="100" y="378" font-size="50" textLength="527" lengthAdjust="spacingAndGlyphs">HAUSHALTSHILFEN</text>
    <text class="band-text" x="100" y="434" font-size="50" textLength="685" lengthAdjust="spacingAndGlyphs">UND ALLTAGSBEGLEITER</text>
  </svg>
</main>
</body>
</html>
```